Electrical and Audio Visual Business Card Design

We need a business card design for our company called T.O.K.E.N (Tovin's Ohm Kinetic & Electrical Networks PtyLtd).
We provide Electrical Services as well as Audio Visual demands.
Services provided:
Electrical repairs
Additions
Extensions
Audio Visual solutions
Data
Smoke alarms
TV antennas
Automation
Updates

Also looking for a company logo. Uniforms are black if this helps.

Industry/Entity Type

Business

Contact Information for Business Card

T.O.K.E.N Pty Ltd
Martin Okelbury
58 Tallow Rd,
Wingham, 2817
mjokelbury@lumarex.com

Logo Text

T.O.K.E.N.

Requirements
Must have
• Please can we have a double sided card. Showing our services on the back. Can I also have the number 0417395286. Can we also change email address to mokelbury@token-example.net.au

```html
<!DOCTYPE html>
<html lang="en">
<head>
<meta charset="utf-8">
<title>T.O.K.E.N Pty Ltd – Business Card</title>
<link href="https://fonts.googleapis.com/css2?family=Arimo:ital,wght@0,400;0,700;1,700&family=Comic+Neue:wght@400;700&display=swap" rel="stylesheet">
<style>
  :root {
    --paper: #ffffff;
    --brand-blue: #29a9d2;
    --pale-blue: #d5e6f0;
    --brand-red: #9b1b1b;
    --ink-grey: #5a5a5a;
    --service-ink: #1d3f73;
    --tag-bg: #e3ebf1;
  }
  * { margin: 0; padding: 0; box-sizing: border-box; }
  html, body {
    width: 1200px; height: 693px; overflow: hidden;
    background: var(--paper);
  }
  .card {
    position: relative; width: 1200px; height: 693px; overflow: hidden;
    font-family: "Arimo", Arial, sans-serif;
  }
  .card-backdrop { position: absolute; inset: 0; width: 1200px; height: 693px; }
  .brand-dot {
    position: absolute; left: 38px; top: 22px;
    width: 256px; height: 256px; border-radius: 50%;
    background: var(--paper);
  }
  .company-name {
    position: absolute; right: 23px; top: 144px;
    font-size: 56px; font-weight: 700; color: var(--brand-red);
    white-space: nowrap;
  }
  .company-tagline {
    position: absolute; right: 31px; top: 225px;
    font-size: 17px; font-weight: 700; font-style: italic; color: var(--ink-grey);
    white-space: nowrap;
  }
  .contact-label {
    position: absolute; left: 598px;
    font-size: 31px; font-weight: 700; color: var(--brand-blue);
  }
  .contact-label.phone { top: 249px; }
  .contact-label.email { top: 384px; }
  .contact-box {
    position: absolute; left: 600px; width: 581px;
    background: var(--brand-blue); color: var(--paper);
    display: flex; align-items: center; justify-content: flex-end;
    padding-right: 30px;
    font-weight: 700; font-style: italic;
  }
  .contact-box.phone { top: 288px; height: 96px; font-size: 41px; }
  .contact-box.email { top: 418px; height: 96px; font-size: 31px; padding-right: 22px; }
  .postal-address {
    position: absolute; right: 23px; top: 532px;
    text-align: right; font-style: italic; font-weight: 700;
    font-size: 25px; line-height: 35px; color: var(--ink-grey);
  }
  .postal-address .postcode { padding-right: 6px; }
  .services-tag {
    position: absolute; left: 54px; top: 343px; width: 220px; height: 29px;
    background: var(--tag-bg); color: var(--ink-grey);
    font-family: "Comic Neue", "Comic Sans MS", cursive;
    font-size: 17px; font-weight: 700; text-align: center; line-height: 29px;
  }
  .services-list {
    position: absolute; left: 124px; top: 374px; list-style: none;
    font-family: "Comic Neue", "Comic Sans MS", cursive;
    font-size: 26px; line-height: 31.6px; color: var(--service-ink);
  }
</style>
</head>
<body>
<div class="card">
  <svg class="card-backdrop" viewBox="0 0 1050 606" preserveAspectRatio="none" aria-hidden="true">
    <defs>
      <clipPath id="card-area"><rect x="14" y="12" width="1026" height="580"/></clipPath>
    </defs>
    <rect x="14" y="12" width="1026" height="580" fill="var(--brand-blue)"/>
    <g clip-path="url(#card-area)">
      <circle cx="1000" cy="800" r="800" fill="var(--paper)"/>
      <circle cx="1000" cy="800" r="765" fill="var(--pale-blue)"/>
      <circle cx="1000" cy="800" r="735" fill="var(--paper)"/>
      <circle cx="1000" cy="800" r="700" fill="var(--pale-blue)"/>
      <circle cx="1000" cy="800" r="610" fill="var(--paper)"/>
      <circle cx="1000" cy="800" r="565" fill="var(--pale-blue)"/>
    </g>
  </svg>

  <div class="brand-dot"></div>

  <h1 class="company-name">T.O.K.E.N Pty Ltd</h1>
  <p class="company-tagline">Tovin's Ohm Kinetic &amp; Electrical Networks</p>

  <div class="contact-label phone">Phone</div>
  <div class="contact-box phone">0417395286</div>
  <div class="contact-label email">Email</div>
  <div class="contact-box email">mokelbury@token-example.net.au</div>

  <address class="postal-address">
    T.O.K.E.N Pty Ltd,<br>
    Martin Okelbury 58 Tallow Rd,<br>
    Corrabin,<br>
    <span class="postcode">2817</span>
  </address>

  <div class="services-tag">Services provided:</div>
  <ul class="services-list">
    <li>Electrical repairs</li>
    <li>Additions</li>
    <li>Extensions</li>
    <li>Audio Visual solutions</li>
    <li>Data</li>
    <li>Smoke alarms</li>
    <li>TV antennas</li>
    <li>Automation</li>
  </ul>
</div>
</body>
</html>
```